Bright Arch Group business card

Bright Arch Group is the parent company of Bright Arch Building, Bright Arch Plumbing and Bright Arch Renovating. We require a sophisticated business card that covers all aspects of the building and plumbing space without using told or construction items.

Industry/Entity Type

Construction Company

Contact Information for Business Card

Gareth Pimley
Director
0472915083
gareth@brightarch.com.au
Www.brightarch.com.au

Font styles to use
Serif
Sans Serif

Colors
3176b5
ffce3e
0692cd
34a7d8
fbee3e
faa54b

Requirements
Must have
• Logo on front
• Logo and details on rear.
Nice to have
• Maybe water mark or shadow effect with logo
Should not have
• Tools or any construction associated items

```html
<!DOCTYPE html>
<html lang="en">
<head>
<meta charset="utf-8">
<title>Bright Arch Group – Business Card</title>
<link rel="stylesheet" href="https://fonts.googleapis.com/css2?family=Questrial&display=swap">
<style>
  :root {
    --bg: #dfe5e8;
    --paper: #f3f5f7;
    --paper-shade: #e4e9ec;
    --navy: #0b1a3b;
    --orange: #fb9606;
    --orange-deep: #c45f06;
    --ink: #141414;
    --white: #ffffff;
  }
  * { margin: 0; padding: 0; box-sizing: border-box; }
  html, body { width: 1200px; height: 1200px; overflow: hidden; background: var(--bg); }
  body { position: relative; font-family: "Questrial", "Century Gothic", sans-serif; color: var(--ink); }

  .card {
    position: absolute;
    left: 185px;
    width: 1006px;
    height: 558px;
    transform: scale(0.824);
    transform-origin: 0 0;
    background: linear-gradient(180deg, var(--white) 0%, var(--paper) 45%, var(--paper-shade) 100%);
    overflow: hidden;
  }
  .card--front { top: 77px; }
  .card--back { top: 628px; }
  .card__shapes { position: absolute; inset: 0; width: 100%; height: 100%; }

  .brand { position: absolute; text-align: center; color: var(--ink); line-height: 1; }
  .brand__name { display: block; font-size: 62px; letter-spacing: 0.24em; }
  .brand__sub { display: block; font-size: 40px; letter-spacing: 0.62em; margin-top: 8px; }
  .card--front .brand { left: 0; right: 0; top: 198px; }

  .site-strip {
    position: absolute; left: 562px; right: 0; top: 508px;
    display: flex; align-items: center; justify-content: center; gap: 14px;
    color: var(--white); font-family: Arial, Helvetica, sans-serif; font-size: 14px;
  }
  .site-strip .dot { background: var(--white); border-radius: 50%; display: inline-block; }

  .brand--mini { left: 26px; top: 470px; width: 262px; text-align: center; color: var(--white); }
  .brand--mini .brand__name { font-size: 26px; letter-spacing: 0.14em; margin-right: -0.14em; }
  .brand--mini .brand__sub { font-size: 19px; letter-spacing: 0.6em; margin: 6px -0.6em 0 0; }

  .person { position: absolute; left: 40px; top: 150px; width: 470px; }
  .person__name { font-size: 58px; font-weight: 400; line-height: 1; letter-spacing: -0.01em; white-space: nowrap; }
  .person__role { font-size: 38px; font-style: italic; margin: 4px 0 0 125px; line-height: 1; }
  .avatar { position: absolute; left: 222px; top: 65px; }

  .contacts { position: absolute; right: 32px; top: 210px; list-style: none; }
  .contacts li { display: flex; align-items: center; justify-content: flex-end; gap: 24px; font-size: 33px; }
  .contacts li + li { margin-top: 32px; }
  .contacts li:nth-child(3) { margin-top: 22px; }
  .contacts .icon { width: 58px; height: 58px; border: 3px solid var(--ink); display: flex; align-items: center; justify-content: center; background: var(--white); }
</style>
</head>
<body>

<section class="card card--front" aria-label="Card front">
  <svg class="card__shapes" viewBox="0 0 1006 558" aria-hidden="true">
    <path fill="var(--navy)" d="M0 321 L266 321 L346 457 L495 457 L545 457 L562 487 L1006 487 L1006 558 L0 558 Z"/>
    <path fill="var(--orange)" d="M308 390 L388 390 L487 558 L407 558 Z"/>
    <path fill="var(--orange-deep)" d="M415 428 L478 428 L555 558 L485 558 Z"/>
  </svg>
  <div class="brand">
    <span class="brand__name">BRIGHT ARCH</span>
    <span class="brand__sub">GROUP</span>
  </div>
  <div class="site-strip">
    <span class="dot" style="width:5px;height:5px"></span>
    <span class="dot" style="width:7px;height:7px"></span>
    <span class="dot" style="width:9px;height:9px"></span>
    <span class="dot" style="width:10px;height:10px"></span>
    <span class="dot" style="width:13px;height:13px"></span>
    <span class="site-strip__url">WWW.BRIGHTARCH.COM.AU</span>
    <span class="dot" style="width:13px;height:13px"></span>
    <span class="dot" style="width:10px;height:10px"></span>
    <span class="dot" style="width:9px;height:9px"></span>
    <span class="dot" style="width:7px;height:7px"></span>
    <span class="dot" style="width:5px;height:5px"></span>
    <span class="dot" style="width:4px;height:4px"></span>
  </div>
</section>

<section class="card card--back" aria-label="Card back">
  <svg class="card__shapes" viewBox="0 0 1006 558" aria-hidden="true">
    <path fill="var(--navy)" d="M402 0 L1006 0 L1006 161 L740 161 L660 68 L465 68 Z"/>
    <path fill="var(--orange-deep)" d="M452 0 L515 0 L590 88 L527 88 Z"/>
    <path fill="var(--orange)" d="M515 0 L600 0 L695 115 L610 115 Z"/>
    <path fill="var(--navy)" d="M0 413 L265 413 L330 496 L560 496 L604 558 L0 558 Z"/>
    <path fill="var(--orange)" d="M308 453 L390 453 L478 558 L408 558 Z"/>
    <path fill="var(--orange-deep)" d="M415 478 L478 478 L555 558 L485 558 Z"/>
  </svg>

  <svg class="avatar" width="80" height="80" viewBox="0 0 80 80" aria-hidden="true">
    <circle cx="40" cy="40" r="39" fill="var(--navy)"/>
    <circle cx="40" cy="31" r="12" fill="var(--white)"/>
    <rect x="23" y="46" width="34" height="16" rx="3" fill="var(--white)"/>
  </svg>

  <div class="person">
    <h1 class="person__name">Gareth Pimley</h1>
    <p class="person__role">Director</p>
  </div>

  <ul class="contacts">
    <li><span>gareth@brightarch.com.au</span>
      <span class="icon"><svg width="40" height="28" viewBox="0 0 40 28" aria-hidden="true"><rect width="40" height="28" fill="var(--ink)"/><path d="M2 2 L20 16 L38 2 M2 26 L15 13 M38 26 L25 13" stroke="var(--white)" stroke-width="2" fill="none"/></svg></span></li>
    <li><span>0472-915-083</span>
      <span class="icon"><svg width="24" height="42" viewBox="0 0 24 42" aria-hidden="true"><rect x="1" y="1" width="22" height="40" rx="4" fill="var(--ink)"/><rect x="4" y="6" width="16" height="27" fill="var(--white)"/><circle cx="12" cy="37" r="2" fill="var(--white)"/></svg></span></li>
    <li><span>www.brightarch.com.au</span>
      <span class="icon"><svg width="40" height="40" viewBox="0 0 40 40" aria-hidden="true"><g fill="none" stroke="var(--ink)" stroke-width="2.5"><circle cx="20" cy="20" r="17"/><ellipse cx="20" cy="20" rx="8" ry="17"/><path d="M3 20 H37 M6 11 H34 M6 29 H34 M20 3 V37"/></g></svg></span></li>
  </ul>

  <div class="brand brand--mini">
    <span class="brand__name">BRIGHT ARCH</span>
    <span class="brand__sub">GROUP</span>
  </div>
</section>

</body>
</html>
```